Plateau UI App Design

We need to have a proper design for a web app that we currently mocked in Powerpoint (will be provided). This PPT contains about 15 slides. The final app will have about 5-6 screens but with context sensitive elements. we would prefer a workflow based UI, i.e. screens should not be clogged but the interface should behave like a wizard or an QX Plateau UI app.

- Design should be flat and should be Plateau UI / Quilt Style (using this as a design language and tiles / colors)
- The final result has to be much more designed, modern and homogeneous than now.
- We would also need a clickable HTML(5) prototype of the design, please let us know how this can be achieved
- Internet connection does not matter for the project, so has to work just within a browser but does not need to connect to a server (could even be local files)
- This does not need to be a fully functional HTML 5 page, after all it is a prototype / screen design, so it would be more like mouse over / clicking / moving to next screen
- If you cannot deliver HTML5 then please suggest providing something that we can edit easily ourselves (e.g. a Powerpoint again)
- TROVE is the name of our product

Target Market(s)

Financial institutions

Industry/Entity Type

Internet

Requirements
Must have
• Plateau UI / Quilt design

```html
<!DOCTYPE html>
<html lang="en">
<head>
<meta charset="utf-8">
<title>Golden Price – Instrument Detail</title>
<link rel="stylesheet" href="https://fonts.googleapis.com/css2?family=Open+Sans:wght@400;600;700&display=swap">
<style>
  :root{
    --stage:#e6e2ec;
    --purple:#7d2fd8;
    --purple-dark:#6520bd;
    --purple-deep:#5a1aa8;
    --purple-line:#9a5ae6;
    --teal:#1db49a;
    --teal-dark:#17977f;
    --panel:#f1f1f1;
    --cell:#dadada;
    --cell-light:#ececec;
    --ink:#333;
    --white:#fff;
    --green:#8fd14f;
  }
  *{box-sizing:border-box;margin:0;padding:0}
  html,body{width:1200px;height:900px;overflow:hidden}
  body{background:var(--stage);font-family:"Open Sans",Arial,sans-serif;color:var(--ink);position:relative}
  .app{position:absolute;left:100px;top:130px;width:1000px;height:640px;background:var(--panel);box-shadow:0 14px 40px rgba(60,20,90,.25);overflow:hidden}

  /* sidebar */
  .sidebar{position:absolute;left:0;top:0;width:170px;height:100%;background:var(--purple)}
  .brand{height:60px;padding:10px 18px;background:var(--purple)}
  .brand-name{font-size:26px;font-weight:700;color:var(--white);line-height:26px;letter-spacing:1px}
  .brand-sub{font-size:11px;color:var(--white);margin-top:2px}
  .nav{list-style:none}
  .nav-item{display:flex;align-items:center;height:38px;padding-left:18px;color:var(--white);font-size:13px}
  .nav-item svg{width:18px;height:18px;margin-right:22px;fill:var(--white);flex:none}
  .nav-item.is-active{background:var(--purple-deep)}
  .sidebar-foot{position:absolute;left:0;right:0;bottom:0;height:260px;background:var(--purple-dark)}

  /* top bar */
  .topbar{position:absolute;left:170px;top:0;width:550px;height:60px;display:flex}
  .tile{background:var(--teal);color:var(--white);display:flex;align-items:center;padding:0 12px;border-right:2px solid var(--teal-dark);white-space:nowrap}
  .tile svg{width:26px;height:26px;fill:none;stroke:var(--white);stroke-width:2;margin-right:14px;flex:none}
  .tile-title{font-size:11px;font-weight:700}
  .tile-sub{font-size:10px}
  .tile-instrument{width:300px}
  .tile-portfolio{flex:1}

  /* main */
  .main{position:absolute;left:170px;top:60px;width:550px;height:580px;background:var(--panel)}
  .toolbar{position:absolute;right:24px;top:10px;display:flex;gap:6px}
  .tool{width:16px;height:16px;border-radius:3px}
  .tool.xls{background:#2e8b57}.tool.pdf{background:#c0392b}.tool.doc{background:#7d2fd8}.tool.share{background:#9e9e9e}
  .help{width:18px;height:18px;border:1.5px solid currentColor;border-radius:50%;font-size:11px;font-weight:700;display:flex;align-items:center;justify-content:center;flex:none}
  .main .help{color:var(--purple);position:absolute;right:24px}
  .card{position:absolute;left:28px;width:474px;background:var(--white);padding:8px 12px 10px 40px}
  .card-icon{position:absolute;left:12px;top:14px;width:18px;height:18px;fill:#999}
  .field{display:flex;margin-bottom:4px}
  .field-label{width:150px;background:var(--cell);font-size:12px;padding:5px 10px;margin-right:4px;white-space:nowrap}
  .field-value{flex:1;background:var(--cell-light);font-size:12px;padding:5px 10px;white-space:nowrap}
  .card-actions{display:flex;justify-content:flex-end;gap:6px;margin-top:2px}
  .round{width:18px;height:18px;border-radius:50%;border:1.5px solid var(--purple);background:var(--white)}

  /* right panel */
  .side-panel{position:absolute;left:720px;top:0;width:280px;height:100%;background:var(--purple);color:var(--white)}
  .export{height:60px;background:var(--teal);display:flex;align-items:center;padding:0 14px}
  .export svg{width:24px;height:24px;fill:none;stroke:var(--white);stroke-width:2;margin-right:14px;flex:none}
  .export .help{margin-left:auto;color:var(--white)}
  .panel-row{display:flex;align-items:center;justify-content:space-between;padding:0 14px;height:30px;border-bottom:1px solid var(--purple-line)}
  .panel-row .help{color:var(--white)}
  .play{width:18px;height:18px;border:1.5px solid var(--white);border-radius:50%;display:flex;align-items:center;justify-content:center}
  .section-title{font-size:12px;font-weight:600;letter-spacing:.5px}
  .history{padding:8px 14px}
  .quote{font-size:12px}
  .quote span{color:#d9c4ff}
  .chart{display:block;margin-top:4px}
  .days{display:flex;gap:3px;margin-top:4px}
  .day{flex:1;background:var(--green);color:var(--white);font-size:9px;text-align:center;height:14px;line-height:14px}
  .params{padding:10px 14px;font-size:11px;line-height:16px}
  .param-group{position:relative;margin-bottom:12px;padding-right:40px;white-space:nowrap}
  .param-group b{font-weight:600}
  .param-icon{position:absolute;right:0;top:4px;width:26px;height:26px;background:var(--purple-dark)}
</style>
</head>
<body>
<div class="app">

  <aside class="sidebar">
    <div class="brand">
      <div class="brand-name">TROVE</div>
      <div class="brand-sub">Data Management</div>
    </div>
    <ul class="nav">
      <li class="nav-item is-active"><svg viewBox="0 0 20 20"><circle cx="10" cy="12" r="7"/><rect x="7" y="2" width="6" height="4"/></svg>Golden Price</li>
      <li class="nav-item"><svg viewBox="0 0 20 20"><circle cx="9" cy="5" r="4"/><path d="M2 19c0-6 3-9 7-9s7 3 7 9z"/></svg>Requests</li>
      <li class="nav-item"><svg viewBox="0 0 20 20"><path d="M2 8l8-6 8 6-8 10z"/></svg>Silver Copies</li>
      <li class="nav-item"><svg viewBox="0 0 20 20"><path d="M2 2h16v16H2zM4 4v5h5V4zm7 0v5h5V4zM4 11v5h5v-5zm7 0v5h5v-5z"/></svg>Plausibility</li>
      <li class="nav-item"><svg viewBox="0 0 20 20"><path d="M10 1l2.6 5.6 6 .6-4.5 4 1.3 6-5.4-3.2-5.4 3.2 1.3-6-4.5-4 6-.6z"/></svg>Policy</li>
    </ul>
    <div class="sidebar-foot"></div>
  </aside>

  <header class="topbar">
    <div class="tile tile-instrument">
      <svg viewBox="0 0 26 26"><path d="M2 2v22h22"/><path d="M5 18l6-7 4 4 8-9"/></svg>
      <div><div class="tile-title">ORLEX CORP 1.75 18 NTS 02/06/17</div><div class="tile-sub">ORX STK | NXSE | Corporate Bond</div></div>
    </div>
    <div class="tile tile-portfolio">
      <svg viewBox="0 0 26 26"><rect x="2" y="8" width="22" height="14"/><path d="M9 8V4h8v4"/></svg>
      <div><div class="tile-title">FIXED Income</div><div class="tile-sub">Portfolio</div></div>
    </div>
  </header>

  <main class="main">
    <div class="toolbar"><span class="tool xls"></span><span class="tool pdf"></span><span class="tool doc"></span><span class="tool share"></span></div>
    <span class="help" style="top:36px">?</span>
    <section class="card card-price" style="top:62px">
      <svg class="card-icon" viewBox="0 0 20 20"><circle cx="10" cy="12" r="7"/><rect x="7" y="2" width="6" height="4"/></svg>
      <div class="field"><span class="field-label">Price Value</span><span class="field-value">187.24</span></div>
      <div class="field"><span class="field-label">Currency</span><span class="field-value">USD</span></div>
      <div class="field"><span class="field-label">Price Date</span><span class="field-value">10.03.2014</span></div>
      <div class="field"><span class="field-label">Quotation Type</span><span class="field-value">Official Close</span></div>
      <div class="field"><span class="field-label">Market</span><span class="field-value">NXSE</span></div>
      <div class="field"><span class="field-label">Data Source</span><span class="field-value">Brightquote</span></div>
      <div class="field"><span class="field-label">Price Unit</span><span class="field-value">Piece</span></div>
      <div class="field"><span class="field-label">IFRS 13</span><span class="field-value">Level 1</span></div>
      <div class="card-actions"><span class="round"></span><span class="round"></span></div>
    </section>
    <span class="help" style="top:328px">?</span>
    <section class="card card-policy" style="top:356px">
      <svg class="card-icon" viewBox="0 0 20 20"><path d="M10 1l2.6 5.6 6 .6-4.5 4 1.3 6-5.4-3.2-5.4 3.2 1.3-6-4.5-4 6-.6z"/></svg>
      <div class="field"><span class="field-label">Pricing Policy</span><span class="field-value">Standard EOD</span></div>
      <div class="field"><span class="field-label">Pricing Method</span><span class="field-value">US Bonds</span></div>
    </section>
  </main>

  <aside class="side-panel">
    <div class="export">
      <svg viewBox="0 0 24 24"><rect x="2" y="4" width="14" height="16"/><path d="M10 12h12M18 8l4 4-4 4"/></svg>
      <div><div class="tile-title">EXPORT</div><div class="tile-sub">12/3/2015 1402</div></div>
      <span class="help">?</span>
    </div>
    <div class="panel-row"><span class="play"><svg width="8" height="8" viewBox="0 0 8 8"><path d="M1 0l7 4-7 4z" fill="#fff"/></svg></span><span class="help">?</span></div>
    <div class="panel-row"><span class="section-title">HISTORY</span><span class="help">?</span></div>
    <div class="history">
      <div class="quote">187.24 <span>+0.87 (0.47%)</span></div>
      <svg class="chart" width="252" height="70" viewBox="0 0 252 70" font-size="7" fill="#fff">
        <text x="0" y="12">187.5</text><text x="0" y="26">187.0</text><text x="0" y="40">186.5</text><text x="0" y="54">186.0</text>
        <g stroke="#9a5ae6" stroke-width="1"><line x1="26" y1="10" x2="252" y2="10"/><line x1="26" y1="24" x2="252" y2="24"/><line x1="26" y1="38" x2="252" y2="38"/><line x1="26" y1="52" x2="252" y2="52"/></g>
        <polyline fill="none" stroke="#fff" stroke-width="1.3" points="28,30 40,22 50,38 62,18 72,34 84,26 96,42 108,20 120,30 132,16 144,36 156,24 168,32 180,14 192,28 204,22 216,34 228,18 240,26 250,12"/>
        <text x="28" y="66">30 Jul</text><text x="62" y="66">31</text><text x="84" y="66">1</text><text x="106" y="66">2</text><text x="130" y="66">3</text><text x="154" y="66">4</text><text x="178" y="66">5</text><text x="216" y="66">6 Aug</text>
      </svg>
      <div class="days"><span class="day">14</span><span class="day">14</span><span class="day">15</span><span class="day">14</span><span class="day">15</span><span class="day">16</span><span class="day">14</span><span class="day">15</span></div>
    </div>
    <div class="panel-row"><span class="section-title">PARAMETERISATION</span><span class="help">?</span></div>
    <div class="params">
      <div class="param-group"><b>Policy</b>: Standard EOD<br><b>Subset</b>: USBonds SS<br><b>Pricing Method</b>: US Bonds<span class="param-icon"></span></div>
      <div class="param-group"><b>Request Profile</b>: Standard EOD<br><b>Selection Profile</b>: Close Sta...<br><b>Plausibility Profile</b>: Standard...<span class="param-icon"></span></div>
      <div class="param-group"><b>Benchmark</b>: FRMI Global Core...<span class="param-icon"></span></div>
    </div>
  </aside>

</div>
</body>
</html>
```